Flyer for teen fitness class at a physiotherapy clinic

We are a passionate Physiotherapy Clinic requiring a flyer to promote our new service a fitness class for teenagers, which is called Youth Move Lab - Motion Posture Tone Power. The aim of the class is to prevents injuries in sports, improve sporting performance and provide safe activity for otherwise inactive teens. The aim of the flyer is to make people aware of this new service and interested in joining. Ideally the Flyer would incorporate blue colours. Our logo must be on the flier, and at least one or two of the photos provided. Our logo is provided in the attachments. Required information : Youth Move Lab: Motion Posture Tone Power, times Mondays and Wednesdays 4 -5. Can be claimed on private health insurance. Expert advice to tailor a program to individual needs. For more information go www.qrvmx.com.au or phone 03)5871 6093.

```html
<!DOCTYPE html>
<html lang="en">
<head>
<meta charset="utf-8">
<title>Youth Move Lab - Motion Posture Tone Power</title>
<link rel="stylesheet" href="https://fonts.googleapis.com/css2?family=Alfa+Slab+One&family=Rokkitt:wght@400;600;700&display=swap">
<style>
  :root {
    --page-bg: #dfe6ea;
    --brand-blue: #3a7fc8;
    --brand-navy: #1f3158;
    --band-grey: #d9d9db;
    --paper: #ffffff;
    --ink: #2b2b2b;
    --sky-top: #4c8fd6;
    --sky-bottom: #a9c9e6;
    --sun-warm: #d9a24a;
    --sun-cool: #b8d3c6;
  }
  * { margin: 0; padding: 0; box-sizing: border-box; }
  html, body { width: 1046px; height: 1200px; overflow: hidden; }
  body {
    background: var(--page-bg);
    font-family: "Rokkitt", Georgia, serif;
    position: relative;
  }
  .flyer {
    position: absolute;
    left: 133px;
    top: 50px;
    width: 780px;
    height: 1100px;
    background: var(--paper);
    overflow: hidden;
  }
  .flyer-shapes { position: absolute; inset: 0; }
  .brand {
    position: absolute;
    left: 56px;
    top: 318px;
    display: flex;
    align-items: center;
    gap: 12px;
    color: var(--brand-navy);
    font-weight: 700;
    font-size: 30px;
    line-height: 1;
  }
  .brand-dot {
    width: 34px; height: 34px; border-radius: 50%;
    background: var(--brand-navy);
  }
  .brand-name small {
    display: block;
    font-size: 30px;
    font-weight: 700;
  }
  .class-title {
    position: absolute;
    left: 46px;
    top: 478px;
    width: 470px;
    color: var(--paper);
  }
  .rule { height: 3px; background: var(--paper); }
  .rule-top { width: 90px; margin-left: 230px; margin-bottom: 14px; }
  .rule-bottom { width: 120px; margin-top: 14px; }
  .class-kicker {
    font-size: 32px;
    font-weight: 600;
    line-height: 0.95;
    text-transform: uppercase;
  }
  .class-name {
    font-family: "Alfa Slab One", Georgia, serif;
    color: var(--brand-navy);
    font-size: 50px;
    line-height: 1.1;
    text-transform: uppercase;
    margin-top: 8px;
  }
  .class-pillars {
    font-size: 19px;
    letter-spacing: 0.5px;
    text-transform: uppercase;
    margin-top: 4px;
  }
  .schedule {
    position: absolute;
    left: 40px;
    top: 870px;
    width: 320px;
    color: var(--brand-navy);
  }
  .schedule-days {
    font-size: 32px;
    font-weight: 700;
    line-height: 0.95;
    text-transform: uppercase;
  }
  .schedule-time {
    font-family: "Alfa Slab One", Georgia, serif;
    font-size: 52px;
    line-height: 1.2;
  }
  .schedule-note {
    margin-top: 22px;
    margin-left: 14px;
    width: 230px;
    font-size: 14px;
    line-height: 1.15;
    color: var(--ink);
    text-transform: uppercase;
  }
  .divider {
    position: absolute;
    left: 390px;
    top: 860px;
    width: 3px;
    height: 190px;
    background: var(--brand-blue);
  }
  .aim {
    position: absolute;
    left: 415px;
    top: 800px;
    width: 340px;
  }
  .aim-title {
    font-family: "Alfa Slab One", Georgia, serif;
    color: var(--brand-blue);
    font-size: 44px;
    line-height: 1;
    letter-spacing: 1px;
  }
  .aim-text {
    margin-top: 12px;
    font-size: 19px;
    line-height: 1.1;
    color: var(--ink);
  }
  .contact {
    position: absolute;
    left: 415px;
    top: 960px;
    color: var(--brand-navy);
  }
  .contact-lead {
    font-size: 22px;
    font-weight: 700;
    text-transform: uppercase;
  }
  .contact-line {
    display: flex;
    align-items: center;
    gap: 10px;
    font-size: 22px;
    color: var(--brand-blue);
    margin-top: 4px;
  }
  .contact-line svg { width: 18px; height: 18px; flex: none; }
  .contact-web { text-transform: uppercase; }
</style>
</head>
<body>
  <main class="flyer">
    <svg class="flyer-shapes" viewBox="0 0 780 1100" width="780" height="1100" aria-hidden="false">
      <defs>
        <linearGradient id="skyFill" x1="0" y1="0" x2="0" y2="1">
          <stop offset="0" stop-color="var(--sky-top)"/>
          <stop offset="1" stop-color="var(--sky-bottom)"/>
        </linearGradient>
        <linearGradient id="sunsetFill" x1="0" y1="1" x2="1" y2="0">
          <stop offset="0" stop-color="var(--sun-warm)"/>
          <stop offset="1" stop-color="var(--sun-cool)"/>
        </linearGradient>
      </defs>
      <rect class="photo-hero" x="0" y="0" width="780" height="620" fill="url(#skyFill)"
            role="img" aria-label="Photo of a smiling teenage girl catching a netball outdoors under a blue sky"/>
      <polygon class="band-grey" points="0,270 640,170 640,315 0,430" fill="var(--band-grey)"/>
      <polygon class="band-blue" points="0,430 780,290 780,600 0,800" fill="var(--brand-blue)"/>
      <polygon class="photo-runner" points="0,800 780,600 780,740 0,806" fill="url(#sunsetFill)"
               role="img" aria-label="Photo of a runner on a trail at sunset"/>
      <polygon class="paper" points="0,806 780,740 780,1100 0,1100" fill="var(--paper)"/>
      <polygon class="corner-navy" points="520,1100 780,1030 780,1100" fill="var(--brand-navy)"/>
    </svg>

    <div class="brand">
      <span class="brand-dot"></span>
      <span class="brand-name">Harbourline<small>Sports Treatment Clinic</small></span>
    </div>

    <section class="class-title">
      <div class="rule rule-top"></div>
      <p class="class-kicker">A fitness class for teenagers</p>
      <h1 class="class-name">Youth Move Lab</h1>
      <p class="class-pillars">Motion | Posture | Tone | Power</p>
      <div class="rule rule-bottom"></div>
    </section>

    <section class="schedule">
      <p class="schedule-days">Mondays &amp;<br>Wednesdays</p>
      <p class="schedule-time">4 -5</p>
      <p class="schedule-note">Can be claimed on private health insurance. Expert advice to tailor a program to individual needs.</p>
    </section>

    <div class="divider"></div>

    <section class="aim">
      <h2 class="aim-title">OUR AIM</h2>
      <p class="aim-text">The aim of the class is to prevents injuries in sports, improve sporting performance and provide safe activity for otherwise inactive teens.</p>
    </section>

    <section class="contact">
      <p class="contact-lead">For more information go</p>
      <p class="contact-line contact-web">
        <svg viewBox="0 0 24 24" aria-hidden="true"><circle cx="12" cy="12" r="9" fill="none" stroke="currentColor" stroke-width="2"/><path d="M3 12h18M12 3c3 3 3 15 0 18M12 3c-3 3-3 15 0 18" fill="none" stroke="currentColor" stroke-width="1.6"/></svg>
        www.qrvmx.com.au
      </p>
      <p class="contact-line">
        <svg viewBox="0 0 24 24" aria-hidden="true"><path d="M6.6 10.8a15.1 15.1 0 0 0 6.6 6.6l2.2-2.2a1 1 0 0 1 1-.25 11.4 11.4 0 0 0 3.6.57 1 1 0 0 1 1 1V20a1 1 0 0 1-1 1A17 17 0 0 1 3 4a1 1 0 0 1 1-1h3.5a1 1 0 0 1 1 1c0 1.25.2 2.46.57 3.6a1 1 0 0 1-.25 1z" fill="currentColor"/></svg>
        (03)5871 6093
      </p>
    </section>
  </main>
</body>
</html>
```